Lark and Fern: Calm Focus and Steady Ground for Everyone Needs a Buissness Card Design

Lark and Fern Community Center is an organization that seeks to bring balance into people's lives. Main services include: guided meditation, group brainstorming, and guided counseling. Lark and Fern combines Eastern practices, i.e. Buddhism, Hinduism, and Taoism, with Western practices: therapy, group brainstorming and healing. We would like a double sided card: 1) front vertical with image, 2) back horizontal with information. The main colors for the card are red, white, black. Different finishes would be nice--please no high gloss. Matte, pearlized, embossing--used tactfully and sparingly would be nice. The card should convey balance/harmony in a modern world.

```html
<!DOCTYPE html>
<html lang="en">
<head>
<meta charset="utf-8">
<title>Lark and Fern – Business Card</title>
<link href="https://fonts.googleapis.com/css2?family=Arimo:wght@400&display=swap" rel="stylesheet">
<style>
  :root {
    --backdrop: #e6e6e6;
    --paper: #ffffff;
    --ink: #111111;
    --accent-red: #ee1c25;
    --faint-peach: #fdebe4;
    --band-black: #000000;
  }
  * { box-sizing: border-box; margin: 0; padding: 0; }
  html, body {
    width: 1200px;
    height: 782px;
    overflow: hidden;
    background: var(--backdrop);
    font-family: "Arimo", Helvetica, Arial, sans-serif;
  }
  .canvas {
    position: relative;
    width: 1200px;
    height: 782px;
  }

  /* Horizontal information side */
  .card-back {
    position: absolute;
    left: 133px;
    top: 340px;
    width: 555px;
    height: 310px;
    background: var(--paper);
    box-shadow: 0 2px 6px rgba(0,0,0,0.12);
    overflow: hidden;
  }
  .card-back__mark {
    position: absolute;
    left: 352px;
    top: 30px;
    width: 238px;
    height: 238px;
  }
  .org-name {
    position: absolute;
    left: 37px;
    top: 44px;
    font-size: 31px;
    font-weight: 400;
    color: var(--ink);
    letter-spacing: 0.2px;
    white-space: nowrap;
  }
  .org-tagline {
    position: absolute;
    left: 38px;
    top: 84px;
    font-size: 13px;
    color: var(--accent-red);
    white-space: nowrap;
  }
  .employee-name {
    position: absolute;
    left: 36px;
    top: 135px;
    font-size: 19px;
    color: var(--accent-red);
  }
  .employee-position {
    position: absolute;
    left: 38px;
    top: 157px;
    font-size: 13px;
    color: var(--ink);
  }
  .contact-list {
    position: absolute;
    left: 36px;
    top: 176px;
    list-style: none;
  }
  .contact-list li {
    display: flex;
    align-items: center;
    height: 20px;
  }
  .contact-list .label {
    width: 29px;
    font-size: 16px;
    color: var(--accent-red);
  }
  .contact-list .value {
    font-size: 13px;
    color: var(--ink);
  }
  .card-back__rule {
    position: absolute;
    left: 0;
    right: 0;
    top: 280px;
    height: 2px;
    background: var(--ink);
  }
  .address {
    position: absolute;
    left: 36px;
    top: 286px;
    font-size: 13px;
    color: var(--ink);
  }

  /* Vertical image side */
  .card-front {
    position: absolute;
    left: 709px;
    top: 83px;
    width: 328px;
    height: 571px;
    background: var(--paper);
    box-shadow: 0 2px 6px rgba(0,0,0,0.12);
    overflow: hidden;
  }
  .card-front__band {
    position: absolute;
    left: 164px;
    top: 0;
    width: 164px;
    height: 100%;
    background: var(--band-black);
  }
  .card-front__disc {
    position: absolute;
    left: 38px;
    top: 159px;
    width: 252px;
    height: 252px;
    border-radius: 50%;
    background: var(--accent-red);
    display: flex;
    align-items: center;
    justify-content: center;
  }
  .card-front__name {
    font-size: 28px;
    color: var(--paper);
    white-space: nowrap;
  }
</style>
</head>
<body>
<main class="canvas">

  <section class="card-back" aria-label="Business card, information side">
    <svg class="card-back__mark" viewBox="0 0 238 238" aria-hidden="true">
      <circle cx="119" cy="119" r="118" fill="var(--faint-peach)"/>
    </svg>

    <h1 class="org-name">Lark and Fern</h1>
    <p class="org-tagline">Calm Focus and Steady Ground for Everyone</p>

    <p class="employee-name">Employee Name</p>
    <p class="employee-position">Your&nbsp; Position</p>

    <ul class="contact-list">
      <li><span class="label">(w)</span><span class="value">www.yourwebsite.com</span></li>
      <li><span class="label">(p)</span><span class="value">012 345 6789</span></li>
      <li><span class="label">(e)</span><span class="value">info@youremail.com</span></li>
      <li><span class="label">(b)</span><span class="value">Your Blog.com</span></li>
    </ul>

    <div class="card-back__rule"></div>
    <p class="address">Your Adress Inc 2nd Lane Ave Marlow, U.S.A</p>
  </section>

  <section class="card-front" aria-label="Business card, image side">
    <div class="card-front__band"></div>
    <div class="card-front__disc">
      <span class="card-front__name">Lark and Fern</span>
    </div>
  </section>

</main>
</body>
</html>
```